1 Page Website Design For Medlyn Savings Club

~~I NEED A WEBSITE LANDING PAGE DESIGNED~~:

TITLE: GET UP TO 75% Off ALL YOUR DIABETIC SUPPLIES GUARANTEED
SUBITITLE: Never Pay Full Price For Your Diabetic Supplies Again!

~~FORM~~:
Choose Your Current Brand Of Diabetic Supplies That You Currently Use To See If They Are Covered Under Our Free Diabetic RX Assistance Program:

~~DROP DOWN MENU~~
Acarbose Up To 75% Off!

Zernovab Tel Up To 75% Off!

Zernovab Tel Xr Up To 54% Off!

Wempu Up To 75% Off!

Orvantel Up To 75% Off!

Quilmor Up To 75% Off!

Tesfunn Up To 75% Off!

Wombeth Up To 75% Off!

Elkrostiv Up To 54% Off!

Irmoskuve Up To 54% Off!

Ulpremo Up To 54% Off!

Fashkelin Up To 75% Off!

Kolvrin Up To 75% Off!

Chlorpropamide Up To 75% Off!

Colesevelam Up To 75% Off!

Pembrath Up To 54% Off!

Qwemt Up To 75% Off!

Desmopressin 52% Off

Sornefil 74% Off

Ferlutham Up To 54% Off!
Mirsolk Up To 75% Off!

Kelmuro Up To 75% Off!

Yibrosel Up To 75% Off!

Glimepiride 66% Off

Glipizide Up To 75% Off!

Glipizide Er Up To 75% Off!

Ventrosimel Up To 75% Off!

Ventrosimel Xr Up To 75% Off!

Brastumol Up To 75% Off!

Brastumol Xl Up To 75% Off!

Pelkirona Up To 75% Off!

Sovrinka Up To 75% Off!

Glyburide Up To 75% Off!

Glyburide Micronized Up To 75% Off!
Twerdo Up To 75% Off!

Omrick Up To 75% Off!

Hestrolu Up To 75% Off!

Pirvetan 50 50 Up To 75% Off!

Pirvetan Up To 75% Off!

Vostrek N Up To 75% Off!

Vostrek R Up To 75% Off!

Insulin Detemir Up To 75% Off!

Insulin Glulisine Up To 75% Off!

Selbrudar Up To 75% Off!

Thebrisu Up To 75% Off!

Kwelbor Up To 75% Off!

Kwelbor Xr Up To 75% Off!

Mostrelo Up To 75% Off!

Pelvouste Up To 75% Off!

Wurmbostel Up To 75% Off!

Trevlu Up To 75% Off!

Hustravel Xr Up To 75% Off!

Privok Up To 75% Off!

Dosharp Up To 75% Off!

Ostrubel Up To 54% Off!

Metformin 73% Off

Talverush Up To 54% Off!

Miglitol Up To 75% Off!

Skevrant Up To 33% Off!

Nateglinide Up To 75% Off!

Wolbrey Up To 75% Off!

Piltrago Up To 75% Off!

Kestrub N Up To 75% Off!

Kestrub R Up To 75% Off!

Harpenu Up To 75% Off!

Blemkarsu Up To 33% Off!

Skirvet Up To 75% Off!

Plembuth Up To 54% Off!

Vurlk Up To 75% Off!

Pioglitazone Up To 75% Off!

Pramlintide Up To 75% Off!

Welhostro Up To 54% Off!

Kuvelst Up To 75% Off!

Dimbrul 20% Off

Repaglinide Up To 75% Off!

Sklavon Up To 75% Off!

Rosiglitazone Up To 75% Off!

Sitagliptin Up To 75% Off!

Humbrev Up To 75% Off!

Fortkavul Up To 75% Off!

Pelbruko Up To 75% Off!

Wiskorb Up To 75% Off!

Tolazamide Up To 75% Off!

Tolbutamide Up To 75% Off!

Breshmuv Up To 54% Off!

Skamvi Up To 75% Off!

Huvelpsor Up To 75% Off!

Komplev Up To 75% Off!

Skyvelmon Up To 15% Off!

Bospenarve Up To 75% Off!

Fresvomel Up To 33% Off!

Drumpal Up To 75% Off!

Spirnak Up To 75% Off!

Premvol Xr Up To 75% Off!

~~~~After they choose one I want this message to pop up~~~~:

YES! ~~NAME OF DRUG~~ IS COVERED UNDER OUR FREE DIABETIC RX PROGRAM!
3 EASY WAYS TO RECEIVE YOUR FREE DIABETIC RX ASSISTANCE VOUCHER:

1. Simply Click Below To Download Your Voucher Right Now!

~~DOWNLOAD VOUCHER NOW~~
2. Enter Your Cell Phone Number And We Will Send The Voucher To You By Text Message Instantly:

3. Enter Your Email And We Will Send The Voucher To Your Email Instantly:

Target Market(s)

People with Diabetes

Number of Pages Required

1 page

Colors

Designer to choose colors to be used in the design.

Requirements
Must have
• must be professional looking and build trust and credibility
Nice to have
• Photos of diabetics...real people
Should not have
• red

```html
<!DOCTYPE html>
<html lang="en">
<head>
<meta charset="utf-8">
<title>Medlyn Savings Club</title>
<link href="https://fonts.googleapis.com/css2?family=Roboto:wght@300;400;500;700&display=swap" rel="stylesheet">
<style>
:root{
  --green:#76b83a;
  --white:#ffffff;
  --ink:#555555;
  --brand-ink:#444444;
  --footer:#2e2e2e;
  --panel:rgba(255,255,255,0.22);
}
*{margin:0;padding:0;box-sizing:border-box}
html,body{width:1200px;height:803px;overflow:hidden}
body{position:relative;font-family:'Roboto',Arial,sans-serif;background:var(--white)}
.site-header{position:absolute;left:0;top:0;width:1200px;height:92px;background:var(--white);border-top:3px solid var(--green)}
.brand{position:absolute;left:86px;top:30px;font-family:'Roboto',Arial,sans-serif;font-weight:400;font-size:22px;color:var(--brand-ink);letter-spacing:0.2px}
.menu-toggle{position:absolute;left:1057px;top:14px;width:56px;height:56px;border:1px solid #ccc;border-radius:50%;display:flex;flex-direction:column;align-items:center;justify-content:center;gap:3px}
.menu-toggle span{display:block;width:16px;height:3px;background:#999}
.hero{position:absolute;left:0;top:92px;width:1200px;height:645px;background:linear-gradient(100deg,#8a4a3a 0%,#b57a66 20%,#9c6b5c 40%,#a97b6d 60%,#8e3f3a 80%,#6e3b30 100%)}
.hero::after{content:"";position:absolute;inset:0;background:rgba(40,30,30,0.35)}
.hero-content{position:absolute;left:0;top:0;width:100%;height:100%;z-index:1}
.hero-title{position:absolute;left:0;width:100%;top:112px;text-align:center;font-size:39px;font-weight:300;color:var(--white)}
.hero-title strong{color:var(--green);font-weight:500}
.hero-subtitle{position:absolute;left:0;width:100%;top:168px;text-align:center;font-size:25px;font-weight:300;color:var(--white)}
.search-panel{position:absolute;left:187px;top:241px;width:826px;height:107px;background:var(--panel);border-radius:3px}
.search-input{position:absolute;left:19px;top:26px;width:641px;height:55px;background:var(--white);border-radius:3px 0 0 3px;font-size:13px;color:var(--ink);text-align:left;padding:24px 18px 0}
.search-input .caret{position:absolute;right:14px;top:26px;width:0;height:0;border-left:5px solid transparent;border-right:5px solid transparent;border-top:5px solid #666}
.search-input .divider{position:absolute;right:40px;top:21px;width:1px;height:15px;background:#aaa}
.search-button{position:absolute;left:660px;top:26px;width:147px;height:55px;background:var(--green);color:var(--white);font-size:20px;font-weight:500;display:flex;align-items:center;justify-content:center;border-radius:0 3px 3px 0}
.dropdown{position:absolute;left:564px;top:411px;width:279px;height:379px;background:var(--green);z-index:3}
.dropdown::before{content:"";position:absolute;right:12px;top:-8px;border-left:8px solid transparent;border-right:8px solid transparent;border-bottom:8px solid var(--green)}
.dropdown-list{list-style:none;position:absolute;left:0;top:0;width:263px;height:100%;overflow:hidden}
.dropdown-list li{height:36px;padding-left:41px;position:relative;font-size:12px;font-weight:500;color:var(--white);line-height:36px;white-space:nowrap}
.dropdown-list li:first-child{margin-top:12px}
.dropdown-list li::before{content:"»";position:absolute;left:19px;top:0;font-size:13px}
.scrollbar{position:absolute;right:6px;top:4px;width:11px;height:368px;background:#f2f2f2;border:1px solid #ddd}
.scrollbar .thumb{position:absolute;left:1px;top:48px;width:7px;height:78px;background:#cfcfcf;border-radius:2px}
.site-footer{position:absolute;left:0;top:737px;width:1200px;height:66px;background:var(--footer)}
.copyright{position:absolute;left:87px;top:28px;font-family:Arial,sans-serif;font-size:12.5px;color:#eee}
.social{position:absolute;left:906px;top:15px;display:flex;gap:7px}
.social span{width:36px;height:36px;border:2px solid #eee;border-radius:50%}
.version{position:absolute;left:1126px;top:39px;font-size:12px;color:#eee}
</style>
</head>
<body>
<header class="site-header">
  <div class="brand">Medlyn Savings Club</div>
  <div class="menu-toggle"><span></span><span></span><span></span></div>
</header>

<section class="hero" role="img" aria-label="Photo of smiling older adults sitting together at home">
  <div class="hero-content">
    <h1 class="hero-title"><strong>Get Up To 75% Off</strong> All Your Diabetic Supplies</h1>
    <p class="hero-subtitle">Never Pay Full Price For Your Diabetic Supplies Again!</p>
    <div class="search-panel">
      <div class="search-input">Enter Your Keyword :<span class="divider"></span><span class="caret"></span></div>
      <div class="search-button">SEARCH</div>
    </div>
  </div>
</section>

<div class="dropdown">
  <ul class="dropdown-list">
    <li>ACARBOSE UP TO 75% OFF!</li>
    <li>ZERNOVAB TEL UP TO 75% OFF!</li>
    <li>QUILMOR UP TO 75% OFF!</li>
    <li>CHLORPROPAMIDE UP TO 75% OFF!</li>
    <li>COLESEVELAM UP TO 75% OFF!</li>
    <li>PEMBRATH UP TO 54% OFF!</li>
    <li>MIRSOLK UP TO 75% OFF!</li>
    <li>KELMURO UP TO 75% OFF!</li>
    <li>YIBROSEL&nbsp; UP TO 75% OFF!</li>
    <li>GLIMEPIRIDE 66% OFF</li>
  </ul>
  <div class="scrollbar"><div class="thumb"></div></div>
</div>

<footer class="site-footer">
  <p class="copyright">© Copy Right -2017 Medlyn Savings Club. All rights reserved.</p>
  <div class="social"><span></span><span></span><span></span><span></span><span></span></div>
  <span class="version">C2</span>
</footer>
</body>
</html>
```